Web Design Project

The client is unsure if they want a completely new design or a design that matches their existing site closely (https://www.talvoinsurance.com.au). So essentially we are looking for some designs that reflect the existing sites shape and colour and some designs that have their own new style. The company will sell three main types of insurance, Car, Bike and Caravan.

Read the complete brief and in the attached document.
The logo is also attached

I have also attached a zip of a few classic cars, if you can incorporate those.

Industry/Entity Type

Insurance

Requirements
Should not have

```html
<!DOCTYPE html>
<html lang="en">
<head>
<meta charset="utf-8">
<title>Talvo Insurance – Classic and Prestige Car &amp; Bike Insurance</title>
<link rel="stylesheet" href="https://fonts.googleapis.com/css2?family=Didact+Gothic&family=Noto+Sans&family=PT+Sans&display=swap">
<style>
  :root {
    --brand-red: #c8141b;
    --brand-red-dark: #8f0c10;
    --heading-red: #b5121b;
    --black: #000;
    --nav-dark: #1a1a1a;
    --text: #111;
    --white: #fff;
    --frame-grey: #a9a9a9;
    --backdrop-light: #f2f2f2;
    --backdrop-mid: #c9c9c9;
    --button-grey: #dcdcdc;
  }
  * { box-sizing: border-box; margin: 0; padding: 0; }
  html, body { width: 1200px; height: 750px; overflow: hidden; }
  body {
    position: relative;
    font-family: "Noto Sans", sans-serif;
    color: var(--text);
    background: linear-gradient(180deg, var(--backdrop-light) 0%, #e6e6e6 55%, var(--backdrop-mid) 100%);
  }
  .backdrop-scene {
    position: absolute; top: 450px; width: 223px; height: 300px;
    background: linear-gradient(180deg, rgba(200,200,200,0) 0%, #a8a8a8 60%, #8d8d8d 100%);
  }
  .backdrop-scene.left { left: 0; }
  .backdrop-scene.right { right: 0; }

  .page { position: absolute; left: 223px; top: 0; width: 750px; height: 750px; background: var(--white); }

  .header { position: absolute; left: 0; top: 0; width: 750px; height: 222px; background: var(--black); }
  .brand-panel {
    position: absolute; left: 0; top: 27px; width: 179px; height: 195px;
    background: linear-gradient(180deg, #e3262c 0%, var(--brand-red) 45%, var(--brand-red-dark) 100%);
    display: flex; align-items: center; justify-content: center; gap: 6px;
  }
  .brand-name {
    font-family: "PT Sans", sans-serif; font-size: 17px; color: var(--white);
    letter-spacing: 0.5px; text-align: center; line-height: 1.05;
  }
  .brand-dot { width: 8px; height: 8px; border-radius: 50%; background: var(--white); }
  .hero {
    position: absolute; left: 179px; top: 0; width: 571px; height: 222px;
    background: linear-gradient(90deg, #000 0%, #3a3a3a 20%, #d9d9d9 45%, #f0f0f0 65%, #8a8a8a 85%, #1b1b1b 100%);
  }
  .hero::after {
    content: ""; position: absolute; left: 0; top: 0; width: 100%; height: 60px;
    background: linear-gradient(180deg, #000 0%, rgba(0,0,0,0) 100%);
  }
  .tagline { position: absolute; left: 203px; top: 6px; color: var(--white); z-index: 2; }
  .tagline h1 { font-family: "Didact Gothic", sans-serif; font-weight: 400; font-size: 24px; line-height: 28px; }
  .tagline p { font-family: "Noto Sans", sans-serif; font-size: 11px; margin-top: 2px; }

  .main-nav {
    position: absolute; left: 179px; top: 222px; width: 571px; height: 36px;
    background: linear-gradient(180deg, #3a3a3a 0%, var(--nav-dark) 100%);
    display: flex; align-items: center;
  }
  .main-nav a {
    font-family: "PT Sans", sans-serif; font-size: 12.5px; color: var(--white);
    text-decoration: none; height: 36px; line-height: 36px; padding: 0 18px;
  }
  .main-nav a.active { background: var(--brand-red); }

  .sidebar { position: absolute; left: 0; top: 222px; width: 179px; }
  .benefits-title {
    font-family: "PT Sans", sans-serif; font-weight: 400; font-size: 16.5px; line-height: 19px;
    color: var(--heading-red); text-align: center; margin-top: 16px;
  }
  .benefits-rule { border: 0; border-top: 2px solid var(--black); margin: 10px 7px 0 7px; }
  .benefits { list-style: none; padding: 5px 5px 0 10px; font-size: 12px; line-height: 14px; }
  .benefits li { margin-bottom: 14px; }
  .quote-button {
    position: absolute; left: 11px; top: 321px; width: 156px; height: 25px;
    background: linear-gradient(180deg, #f2f2f2 0%, var(--button-grey) 100%);
    font-family: "PT Sans", sans-serif; font-size: 16.5px; color: var(--heading-red);
    line-height: 25px; padding-left: 6px; text-decoration: none;
  }
  .call-us { position: absolute; left: 16px; top: 376px; width: 150px; }
  .call-us svg { position: absolute; left: 0; top: 0; }
  .call-us p {
    font-family: "PT Sans", sans-serif; font-size: 16.5px; line-height: 19px;
    color: var(--heading-red); text-align: center; padding-left: 12px;
  }

  .content { position: absolute; left: 194px; top: 280px; width: 545px; }
  .content h2 {
    font-family: "PT Sans", sans-serif; font-weight: 400; font-size: 16.5px; color: var(--heading-red);
  }
  .content p.welcome-copy { font-size: 12px; line-height: 13.9px; margin-top: 15px; }
  .events-title { position: absolute; top: 175px; }
  .event-photo {
    position: absolute; top: 215px; height: 157px; border: 3px solid var(--frame-grey);
  }
  .event-photo.race { left: 0; width: 170px; background: linear-gradient(180deg, #dfe3e6 0%, #8c9196 55%, #5e5356 100%); }
  .event-photo.show { left: 178px; width: 184px; background: linear-gradient(180deg, #d6d9dc 0%, #9ea3a0 45%, #7d7574 100%); }
  .event-photo.cheque { left: 370px; width: 174px; background: linear-gradient(135deg, #e9a23a 0%, #8fb14a 45%, #2a3f7a 70%, #e7e3dc 100%); }

  .footer {
    position: absolute; left: 0; top: 673px; width: 750px; height: 77px;
    background: linear-gradient(180deg, #000 0%, #111 50%, #3a3a3a 100%);
  }
  .footer-nav { position: absolute; left: 189px; top: 35px; display: flex; gap: 0; }
  .footer-nav a {
    font-family: "PT Sans", sans-serif; font-size: 7px; color: var(--white);
    text-decoration: none; margin-right: 23px;
  }
</style>
</head>
<body>
  <div class="backdrop-scene left" role="img" aria-label="Faded silver sports car on a road"></div>
  <div class="backdrop-scene right" role="img" aria-label="Faded sports motorbike"></div>

  <div class="page">
    <header class="header">
      <div class="hero" role="img" aria-label="Smiling family of four beside a white SUV"></div>
      <div class="tagline">
        <h1>Insure with an Enthusiast</h1>
        <p>Classic and Prestige Car &amp; Bike Insurance</p>
      </div>
      <div class="brand-panel">
        <span class="brand-dot"></span>
        <span class="brand-name">TALVO<br>INSURANCE</span>
      </div>
    </header>

    <nav class="main-nav">
      <a class="active" href="#">HOME</a>
      <a href="#">ABOUT US</a>
      <a href="#">INSURANCE</a>
      <a href="#">EVENTS</a>
      <a href="#">CLUBS</a>
      <a href="#">LINKS</a>
      <a href="#">CONTACT US</a>
    </nav>

    <aside class="sidebar">
      <h3 class="benefits-title">OUR POLICY<br>BENEFITS</h3>
      <hr class="benefits-rule">
      <ul class="benefits">
        <li>Agreed Value</li>
        <li>New replacement vehicle in 2 years</li>
        <li>Choice of Repairer</li>
        <li>Lifetime guarantee for repairs</li>
        <li>Pay premiums by installments</li>
        <li>Flexible coverage</li>
        <li>Salvage retained by you on vehicles over 30 years</li>
      </ul>
      <a class="quote-button" href="#">REQUEST A QUOTE</a>
      <div class="call-us">
        <svg width="30" height="46" viewBox="0 0 30 46" aria-hidden="true">
          <path d="M8 2 C2 6 0 16 2 26 C4 36 10 44 18 45 L24 38 C21 35 17 36 15 34 C12 28 11 20 12 14 C14 12 18 12 19 9 L16 1 Z" fill="var(--heading-red)"/>
        </svg>
        <p>CALL US AT<br>033-4120-7736</p>
      </div>
    </aside>

    <main class="content">
      <h2>WELCOME TO OUR SITE</h2>
      <p class="welcome-copy">Lorem ipsum dolor sit amet, consectetuer adipiscing elit, sed diam nonummy nibh euismod tincidunt ut laoreet dolore magna aliquam erat volutpat. Ut wisi enim ad minim veniam, quis nostrud exerci tation ullamcorper suscipit lobortis nisl ut aliquip ex ea commodo consequat.<br>Lorem ipsum dolor sit amet, consectetuer adipiscing elit, sed diam nonummy nibh euismod tincidunt ut laoreet dolore magna aliquam erat volutpat. Ut wisi enim ad minim veniam, quis nostrud exerci tation ullamcorper suscipit lobortis nisl ut aliquip ex</p>
      <h2 class="events-title">UPCOMING EVENTS</h2>
      <div class="event-photo race" role="img" aria-label="Stock race cars on a speedway track"></div>
      <div class="event-photo show" role="img" aria-label="Classic car show in a parking lot"></div>
      <div class="event-photo cheque" role="img" aria-label="Two people presenting a charity cheque"></div>
    </main>

    <footer class="footer">
      <nav class="footer-nav">
        <a href="#">HOME</a>
        <a href="#">ABOUT US</a>
        <a href="#">INSURANCE</a>
        <a href="#">EVENTS</a>
        <a href="#">CLUBS</a>
        <a href="#">LINKS</a>
        <a href="#">CONTACT US</a>
        <a href="#">SITEMAP</a>
      </nav>
    </footer>
  </div>
</body>
</html>
```